OBW Crestmark Shipping Limited

We need the buissnes card to be very exclusive. As we are all young in our company. We need this to be the gate to make our clients feel deep interest for us.

We are focused in as International Trade advisors, and our products go from Oil Tanker Ships to Rubber balls for dogs.

Our Slogan is Trading Near and Far.
And our main marketing will be through Internet.

We were stablished in 2009 In Mexico and we also have offices in Hong Kong.
We have representatives in China and Europe.

Target Market(s)

Is every company or Individual that wants to develop an International Project or product development or Logistic service of Goods and people.
Some of our current projects are Ship Brokerage, Mine Brokerage, Real State and Product Pormotional development.

Industry/Entity Type

It Company

Requirements
Must have
• Our Logo and slogan, and make the card accoriding to the logo.
Nice to have
• Our Colors

```html
<!DOCTYPE html>
<html lang="en">
<head>
<meta charset="utf-8">
<title>OBW Crestmark Shipping Limited – Business Card</title>
<link href="https://fonts.googleapis.com/css2?family=Noto+Sans:wght@400;600&display=swap" rel="stylesheet">
<style>
  :root {
    --backdrop: #8a8a8a;
    --card: #ffffff;
    --brand-green: #8dc63f;
    --brand-blue: #1a8fce;
    --map-tint: #f1f2f3;
  }
  html, body {
    margin: 0;
    width: 1200px;
    height: 900px;
    overflow: hidden;
    background: var(--backdrop);
    font-family: "Noto Sans", Verdana, sans-serif;
  }
  .business-card {
    position: absolute;
    left: 180px;
    top: 192px;
    width: 840px;
    height: 516px;
    background: var(--card);
    box-shadow: 0 10px 28px rgba(0,0,0,0.35);
    overflow: hidden;
  }
  .world-map {
    position: absolute;
    left: 150px;
    top: -70px;
    width: 620px;
    height: 620px;
    border-radius: 50%;
    background: radial-gradient(circle at 50% 45%, var(--map-tint) 0%, #f6f6f7 60%, rgba(255,255,255,0) 72%);
  }
  .accent-band {
    position: absolute;
    left: 0;
    bottom: 0;
    width: 100%;
    height: 50px;
    background: var(--brand-green);
  }
  .holder {
    position: absolute;
    left: 420px;
    top: 42px;
    margin: 0;
    color: var(--brand-blue);
    font-size: 15px;
    line-height: 1.2;
    text-align: right;
  }
  .holder span { display: block; }
  .brand-dot {
    position: absolute;
    left: 260px;
    top: 188px;
    width: 140px;
    height: 140px;
    border-radius: 50%;
    background: var(--brand-blue);
  }
  .brand-name {
    position: absolute;
    left: 436px;
    top: 212px;
    margin: 0;
    color: var(--brand-green);
    font-size: 64px;
    font-weight: 600;
    line-height: 1;
    letter-spacing: 3px;
  }
  .brand-slogan {
    position: absolute;
    left: 440px;
    top: 282px;
    margin: 0;
    color: var(--brand-blue);
    font-size: 14px;
    letter-spacing: 0.4px;
  }
  .contact {
    position: absolute;
    left: 440px;
    top: 340px;
    margin: 0;
    padding: 0;
    list-style: none;
    color: var(--brand-blue);
    font-size: 19px;
    line-height: 24px;
  }
</style>
</head>
<body>
  <section class="business-card" aria-label="OBW Crestmark Shipping Limited business card">
    <div class="world-map" role="img" aria-label="Faint world map in the card background"></div>

    <p class="holder">
      <span>Daniel Forsythe</span>
      <span>Director</span>
    </p>

    <div class="brand-dot" aria-hidden="true"></div>
    <p class="brand-name">OBW</p>
    <p class="brand-slogan">Trading Near and Far</p>

    <ul class="contact">
      <li>Tel: 0412 586 903</li>
      <li>Fax: 07 5123 4400</li>
      <li>Email: daniel@obw.com.au</li>
      <li>obw.com.au</li>
    </ul>

    <div class="accent-band"></div>
  </section>
</body>
</html>
```